Web re-design project for web software development agency

We need to re-design our existing website (www.tovenmedia.co.uk), and are going to start using a shorter domain (www.toven.com).
We have been in business for 8 years and it's time for an update.

We are based at Harrowmede Court (home of the code breakers). We specialise in writing software for the web. Over the years we have built up a healthy customer base and it is time to incorporate the features we build for our customers into our own site (e.g. social media).

We have a team of 8 talented developers with varied skills including: apps for mobile; complex server side software; front-end software; eCommerce software; specialised web based applications; integration software; hardware support; consultancy services. Our customers are diverse (e.g. banking; commerce; veterinary; R&D; health sector; law; accounting; film industry etc.).

Our current colour scheme is blue, white and green although we are not averse to moving away from these colours. We will also be dropping the DESIGN from our name and logo. Revised logo will be attached.

The site needs to be modern, sophisticated and leading edge. We want to show visitors to the site that we are a professional organisation.
Updates

Our logo in PSD format has been uploaded. Please drop the word DESIGN from the logo.

The deliverable for this project is a PSD (ideally we would like to see how the home page, portfolio page, resources page with mugshots, and forms are going to look).

Many thanks,
Tom

Please DO NOT include a Careers section 

We will also need a "meet our team" section with spaces for 10 photographs as well as some space underneath them so that we can add a short paragraph for each one of them.

Target Market(s)

Mainly large corporations needing bespoke web software, or generally complex projects (for anyone).

Industry/Entity Type

Software

Requirements
Must have
• We would like a home page designed that has the following elements on it:
- Show the new cookie compliance policy displayed probably in the top of the page (will disappear).
- A client Testimonial.
- Pricing icon.
- Social media Links.
- A Quote section in expand/collapse field as in (http://www.quillbrook-online.co.uk/our-services.shtml)

We would also like a portfolio page that showcases our clients in an interesting way.

Finally, we would like a form design that we can use throughout the site (i.e. how should buttons, radio buttons, checkboxes, dropdowns, text areas etc. look)?
Nice to have
• A page that follows these guidelines:
http://www.pagerivet.com/the-anatomy-of-a-perfect-landing-page

Here are a few examples of sites in our sector that we like:
- http://www.tidewell-studio.com/
- http://plinthos.co.uk/
- http://www.fernaxis.com/services/web-development (nice contact us page)
- http://www.quillbrook-online.co.uk/
- http://www.lumsa.com/
- http://www.netmoxa.co.uk/
Should not have
• No flash elemets. If anything, we will use html5.

```html
<!DOCTYPE html>
<html lang="en">
<head>
<meta charset="utf-8">
<title>Toven – Web Software Development</title>
<link href="https://fonts.googleapis.com/css2?family=PT+Sans:ital,wght@0,400;0,700;1,400&display=swap" rel="stylesheet">
<style>
:root{
  --blue:#1a7cc4;
  --blue-dark:#0c5ea3;
  --blue-light:#3aa0e6;
  --olive:#8c9a1c;
  --lime:#b7cf3a;
  --lime-dark:#8fae1f;
  --text:#555;
  --text-dark:#333;
  --panel:#ececec;
  --footer:#363636;
  --white:#fff;
}
*{margin:0;padding:0;box-sizing:border-box}
html,body{width:1114px;height:1200px;overflow:hidden;background:#fff}
body{font-family:"PT Sans",Arial,sans-serif;color:var(--text)}
.stage{position:relative;width:1100px;height:1185px;transform:scale(1.0127);transform-origin:0 0;overflow:hidden}
.abs{position:absolute}

/* header */
.site-header{left:0;top:0;width:1100px;height:98px;background:radial-gradient(ellipse at 70% 30%,#3ba3e6 0%,#1a7fcc 45%,#0f63ab 100%)}
.brand{left:71px;top:31px;display:flex;align-items:center;gap:10px}
.brand-square{width:35px;height:35px;background:var(--lime)}
.brand-name{font-size:31px;font-weight:700;color:var(--white);letter-spacing:1px;line-height:1}
.search{left:850px;top:36px;width:180px;height:25px;background:#fff;border:1px solid #c9d6e0;border-radius:2px;font-size:11px;font-style:italic;color:#888;padding:5px 12px}
.search svg{position:absolute;right:7px;top:6px}

/* nav */
.nav-band{left:0;top:98px;width:1100px;height:72px;border-top:3px solid #555;background:linear-gradient(#fafafa,#efefef)}
.main-nav{left:68px;top:101px;display:flex;height:69px}
.main-nav a{display:block;padding:0 17px;line-height:70px;font-size:14px;color:var(--text-dark);text-decoration:none;border-right:1px solid #dcdcdc}
.main-nav a:last-child{border-right:0}
.main-nav a.is-active{background:#fff;color:var(--blue);padding:0 23px}
.quote-tab{left:851px;top:131px;width:178px;height:39px;background:linear-gradient(#e8e8e8,#d9d9d9);border-radius:6px 6px 0 0;font-size:16px;color:var(--blue);padding:9px 0 0 64px}
.quote-tab svg{position:absolute;left:18px;top:-8px}

/* hero */
.hero{left:0;top:170px;width:1100px;height:275px;background:linear-gradient(#f4f4f4,#fdfdfd 60%,#eeeeee)}
.hero-art{left:60px;top:180px;width:540px;height:255px;background:radial-gradient(ellipse at 45% 55%,#cfe3f2 0%,#e9eef2 45%,rgba(245,245,245,0) 75%)}
.hero-title{left:489px;top:229px;font-size:21.5px;line-height:30px;color:var(--blue);text-transform:uppercase}
.btn-lime{background:linear-gradient(#d2e35b,#a9c42a);color:#3c4710;border-radius:5px;box-shadow:0 2px 3px rgba(0,0,0,.25);font-size:13px;text-transform:uppercase;text-align:center}
.hero-btn{left:849px;top:304px;width:87px;height:34px;line-height:34px}
.slider-dots{left:875px;top:412px;display:flex;gap:18px}
.slider-dots span{width:13px;height:13px;border-radius:50%;background:#bdbdbd;box-shadow:inset 0 1px 2px rgba(0,0,0,.3)}
.slider-dots span.is-current{background:var(--blue)}

/* welcome */
.section-title{font-size:19.5px;color:var(--blue);font-weight:400;text-transform:uppercase}
.section-title em{font-style:normal;color:var(--olive)}
.welcome-title{left:71px;top:482px}
.body-copy{font-size:11.5px;line-height:20px;text-align:justify;color:var(--text)}
.welcome-copy{left:71px;top:518px;width:636px}
.pricing{left:728px;top:473px;width:297px;height:134px;border-radius:5px;background:linear-gradient(#c9e67c,#9fcc4a);box-shadow:inset 0 0 0 1px rgba(255,255,255,.5)}
.pricing-art{left:8px;top:14px;width:76px;height:104px;border-radius:6px;background:linear-gradient(#38c5d8,#1491b0)}
.pricing h3{position:absolute;left:92px;top:14px;font-size:16px;font-weight:400;color:#3f4a14}
.pricing p{position:absolute;left:92px;top:45px;width:192px;font-size:11.5px;line-height:16px;color:#4a5420;text-align:justify}
.pricing-btn{position:absolute;left:93px;top:99px;width:192px;height:24px;border-radius:5px;background:linear-gradient(#fff,#dedede);font-size:11.5px;line-height:24px;text-align:center;color:#555;box-shadow:0 1px 2px rgba(0,0,0,.2)}
.divider{left:68px;top:640px;width:961px;height:1px;background:#d8d8d8}

/* services */
.services-title{left:71px;top:659px}
.services-copy{left:71px;top:695px;width:958px}
.service{display:flex;align-items:center;gap:14px;color:var(--olive);font-size:18px;line-height:22px;text-transform:uppercase}
.service-icon{width:36px;height:46px;border-radius:4px;background:linear-gradient(#e8e8e8,#a8a8a8)}

/* panels */
.panel{background:var(--panel);border-radius:5px}
.testimonials{left:72px;top:838px;width:382px;height:178px}
.works{left:473px;top:838px;width:552px;height:178px}
.panel h2{position:absolute;left:13px;top:16px}
.quote{position:absolute;left:14px;top:50px;width:351px;font-size:12.5px;line-height:20px;font-style:italic;color:#666;text-align:justify}
.quote-mark{font-size:18px;color:#888}
.quote-author{position:absolute;right:20px;top:144px;font-size:12.5px;color:#555}
.quote-author b{color:var(--text-dark)}
.work{position:absolute;top:55px;width:114px;text-align:center;font-size:12px;font-style:italic;color:#666}
.work-shot{width:114px;height:87px;border:1px solid #aaa;box-shadow:0 1px 3px rgba(0,0,0,.25);margin-bottom:6px}

/* cookie bar */
.cookie-bar{left:74px;top:1040px;width:953px;height:54px;background:#fff;border:1px solid #ddd;border-bottom:0;display:flex;align-items:center}
.cookie-bar p{font-size:14px;color:var(--text-dark);margin-left:15px}
.cookie-btn{position:absolute;left:816px;top:12px;width:97px;height:26px;line-height:26px;font-size:13px;color:#fff;font-weight:700;background:linear-gradient(#8ed05a,#4ea623);text-transform:uppercase}

/* footer */
.site-footer{left:0;top:1094px;width:1100px;height:91px;background:var(--footer);border-top:2px solid #222}
.footer-nav{left:73px;top:1115px;font-size:12px;color:#ddd}
.footer-nav span{color:#999;margin:0 7px}
.copyright{left:73px;top:1143px;font-size:12px;color:#ccc}
.social{left:855px;top:1118px;display:flex;gap:10px}
.social span{width:36px;height:36px;border-radius:50%;background:#fff;box-shadow:0 0 0 2px #ddd}

/* side tabs */
.side-tab{left:1066px;width:36px;border-radius:6px 0 0 6px;color:#fff;font-size:14px;writing-mode:vertical-rl;transform-origin:center;display:flex;align-items:center;justify-content:center;text-transform:uppercase;letter-spacing:.5px}
.side-tab span{transform:rotate(180deg)}
.tab-touch{top:607px;height:118px;background:linear-gradient(90deg,#4cb3ee,#1a7cc4)}
.tab-share{top:740px;height:75px;background:linear-gradient(90deg,#c1cf4b,#8c9a1c)}
</style>
</head>
<body>
<div class="stage">
  <header class="site-header abs">
  </header>
  <div class="brand abs"><span class="brand-square"></span><span class="brand-name">TOVEN</span></div>
  <div class="search abs">Search
    <svg width="12" height="12" viewBox="0 0 12 12"><circle cx="5" cy="5" r="3.5" fill="none" stroke="#aaa" stroke-width="1.4"/><line x1="7.5" y1="7.5" x2="11" y2="11" stroke="#aaa" stroke-width="1.6"/></svg>
  </div>

  <div class="nav-band abs"></div>
  <nav class="main-nav abs">
    <a class="is-active" href="#">HOME</a>
    <a href="#">ABOUT US</a>
    <a href="#">OUR SERVICES</a>
    <a href="#">TECHNOLOGY</a>
    <a href="#">PORTFOLIO</a>
    <a href="#">OUR TEAM</a>
    <a href="#">CONTACT US</a>
  </nav>
  <div class="quote-tab abs">
    <svg width="32" height="40" viewBox="0 0 32 40"><rect x="3" y="4" width="22" height="32" fill="#fff" stroke="#999" transform="rotate(-8 14 20)"/><line x1="8" y1="14" x2="22" y2="12" stroke="#bbb"/><line x1="8" y1="19" x2="22" y2="17" stroke="#bbb"/><line x1="9" y1="24" x2="22" y2="22" stroke="#bbb"/><line x1="20" y1="34" x2="30" y2="6" stroke="#555" stroke-width="2"/></svg>
    GET A QUOTE
  </div>

  <section class="hero abs"></section>
  <div class="hero-art abs" role="img" aria-label="Glossy blue service icons floating in front of faded browser windows"></div>
  <h1 class="hero-title abs" style="font-weight:400">We can help ensure your website is usable<br>and standards compliant.</h1>
  <div class="hero-btn btn-lime abs">View more</div>
  <div class="slider-dots abs"><span class="is-current"></span><span></span><span></span><span></span><span></span></div>

  <h2 class="section-title welcome-title abs">Welcome to <em>Toven</em></h2>
  <p class="body-copy welcome-copy abs">Nam libero tempore, cum soluta nobis est eligendi optio cumque nihil impedit quo minus id quod maxime placeat facere possimus, omnis voluptas assumenda est, omnis dolor repellendus. Temporibus autem quibusdam et aut officiis debitis aut rerum necessitatibus saepe eveniet ut et voluptates repudiandae sint et molestiae non recusandae. Itaque earum rerum hic tenetur a sapiente delectus, ut aut reiciendis voluptatibus. Itaque earum rerum hic tenetur a sapiente delectus, ut aut reiciendis voluptatibus maiores alias consequatur aut perferendis doloribus asperiores repellat.</p>

  <aside class="pricing abs">
    <div class="pricing-art abs" role="img" aria-label="Large glossy turquoise dollar sign"></div>
    <h3>VIEW OUR PRICING</h3>
    <p>Temporibus autem quibusdam et aut officiis debitis aut rerum necessitatibus saepe eveniet.</p>
    <div class="pricing-btn">Click here for View more details</div>
  </aside>

  <div class="divider abs"></div>

  <h2 class="section-title services-title abs">Our services</h2>
  <p class="body-copy services-copy abs" style="text-align:left">At vero eos et accusamus et iusto odio dignissimos ducimus qui blanditiis praesentium voluptatum deleniti atque corrupti quos dolores et quas molestias excepturi sint occaecati cupiditate non provident, similique sunt in culpa qui officia deserunt mollitia animi, id est laborum et dolorum fuga. Et harum quidem rerum facilis est et expedita distinctio.</p>

  <div class="service abs" style="left:76px;top:765px"><span class="service-icon" role="img" aria-label="Brushes in a glass jar"></span>Design</div>
  <div class="service abs" style="left:245px;top:765px"><span class="service-icon" role="img" aria-label="Crossed hammer and wrench"></span>Development</div>
  <div class="service abs" style="left:468px;top:767px"><span class="service-icon" role="img" aria-label="Bar chart report"></span>Project<br>Management</div>
  <div class="service abs" style="left:707px;top:769px"><span class="service-icon" role="img" aria-label="Computer case with globe"></span>IT<br>Solutions</div>
  <div class="service abs" style="left:899px;top:769px"><span class="service-icon" style="width:32px" role="img" aria-label="Headset"></span>Ongoing<br>Support</div>

  <section class="testimonials panel abs">
    <h2 class="section-title">Testimonials</h2>
    <p class="quote"><span class="quote-mark">“</span> Taque earum rerum hic tenetur a sapiente delectus, ut aut reiciendis voluptatibus. Itaque earum rerum hic tenetur a sapiente delectus, ut aut reiciendis voluptatibus maiores alias consequatur aut perferendis doloribus asperiores repellat. <span class="quote-mark">”</span></p>
    <p class="quote-author">- <b>Marcus</b> consequatu delect</p>
  </section>

  <section class="works panel abs">
    <h2 class="section-title">Our works</h2>
    <div class="work" style="left:13px"><div class="work-shot" role="img" aria-label="Website screenshot, pale blue dashboard" style="background:linear-gradient(#dbe7f1,#c3d4e3)"></div>Enetur sapien</div>
    <div class="work" style="left:148px"><div class="work-shot" role="img" aria-label="Website screenshot, white page with blue header" style="background:linear-gradient(#eef2f7,#fafafa)"></div>Vitae dicta</div>
    <div class="work" style="left:282px"><div class="work-shot" role="img" aria-label="Website screenshot, white document page with yellow bar" style="background:linear-gradient(#fbf2c4 0,#fff 12%,#f4f4f4)"></div>Nemo enim</div>
    <div class="work" style="left:416px"><div class="work-shot" role="img" aria-label="Website screenshot, football club site with sky and grass" style="background:linear-gradient(#3e9be0,#a7d8f2 40%,#8fcf53 55%,#e9f1f8)"></div>Quia voluptas</div>
  </section>

  <div class="cookie-bar abs">
    <svg width="26" height="26" viewBox="0 0 26 26" style="margin-left:21px"><circle cx="13" cy="13" r="12" fill="#3d86d6"/><circle cx="13" cy="7.5" r="1.8" fill="#fff"/><rect x="11.4" y="11" width="3.2" height="9" fill="#fff"/></svg>
    <p>This site uses cookies to store information on your computer. See our cookie policy for further details on how to block cookies</p>
    <div class="cookie-btn btn-lime">I like this</div>
  </div>

  <footer class="site-footer abs"></footer>
  <div class="footer-nav abs">Home<span>|</span>About Us<span>|</span>Our Services<span>|</span>Technology<span>|</span>Portfolio<span>|</span>Jobs<span>|</span>Contact Us</div>
  <div class="copyright abs">Copyright © 2012 www.toven.com &nbsp;&nbsp; All rights reserved.</div>
  <div class="social abs" aria-label="Social media links"><span></span><span></span><span></span><span></span></div>

  <div class="side-tab tab-touch abs"><span>Get in touch</span></div>
  <div class="side-tab tab-share abs"><span>Share</span></div>
</div>
</body>
</html>
```